Pro-life non-profit needs a dynamic poster design for their Christmas Gala.

We need a poster design which plays off the name of the event, The Winter Lantern. The Winter Lantern, of course is the Baby Jesus. Our cause supports unborn children in Iowa. The gala will include a concert of popular Christmas music sung by top soloists backed by an orchestra. An original commissioned song, The Winter Lantern, will be premiered. Purple and gold colors immediately come to mind, but a designer should not feel constrained on colors. We need an editable design w/fonts. Photoshop w/layers or Illustrator files are good.

```html
<!DOCTYPE html>
<html lang="en">
<head>
<meta charset="utf-8">
<title>The Winter Lantern – A Pro-Life Christmas Gala</title>
<link href="https://fonts.googleapis.com/css2?family=Great+Vibes&family=Montserrat:ital,wght@0,400;0,500;0,700;0,800;1,400&display=swap" rel="stylesheet">
<style>
  :root {
    --night: #0d0714;
    --plum: #3a1248;
    --violet: #6a2a8a;
    --magenta: #a0307a;
    --gold: #e7c98a;
    --white: #ffffff;
    --footer-text: #3b1a55;
  }
  * { margin: 0; padding: 0; box-sizing: border-box; }
  html, body { width: 900px; height: 1200px; overflow: hidden; background: var(--night); }
  .poster {
    position: relative;
    width: 900px;
    height: 1200px;
    overflow: hidden;
    font-family: "Montserrat", Arial, sans-serif;
    color: var(--white);
    text-align: center;
  }
  .bokeh-backdrop {
    position: absolute;
    inset: 0 0 100px 0;
    background:
      radial-gradient(circle at 30% 35%, rgba(160,48,122,.55), transparent 30%),
      radial-gradient(circle at 60% 25%, rgba(106,42,138,.6), transparent 35%),
      radial-gradient(circle at 80% 50%, rgba(58,18,72,.7), transparent 40%),
      radial-gradient(circle at 20% 60%, rgba(90,30,110,.5), transparent 35%),
      radial-gradient(ellipse at 50% 100%, rgba(120,40,90,.35), transparent 45%),
      var(--night);
  }
  .presenter {
    position: absolute; top: 24px; left: 0; right: 0;
    font-style: italic; font-size: 20px; line-height: 28px;
  }
  .title {
    position: absolute; top: 110px; left: 0; right: 0;
    font-family: "Great Vibes", cursive;
    color: var(--gold);
    font-size: 150px; line-height: 150px;
    font-weight: 400;
  }
  .title span { display: block; }
  .title .second { margin-top: -10px; }
  .subtitle-box {
    position: absolute; top: 462px; left: 225px; width: 450px; height: 62px;
    border: 2px solid var(--white);
    font-size: 23px; letter-spacing: 1px; line-height: 58px; font-weight: 500;
  }
  .date { position: absolute; top: 552px; left: 0; right: 0; font-size: 38px; font-weight: 700; }
  .doors { position: absolute; top: 606px; left: 0; right: 0; font-size: 25px; }
  .venue { position: absolute; top: 638px; left: 0; right: 0; font-size: 25px; }
  .pricing { position: absolute; top: 700px; left: 0; right: 0; font-size: 25px; }
  .highlights { position: absolute; top: 760px; left: 0; right: 0; font-size: 40px; font-weight: 800; }
  .speaker-label { position: absolute; top: 838px; left: 0; right: 0; font-size: 25px; }
  .speaker-name { position: absolute; top: 870px; left: 0; right: 0; font-size: 28px; font-weight: 700; }
  .seating { position: absolute; top: 962px; left: 0; right: 0; font-size: 21px; font-weight: 800; letter-spacing: .5px; }
  .footer {
    position: absolute; left: 0; right: 0; bottom: 0; height: 100px;
    background: var(--white); color: var(--footer-text);
    font-size: 22px; line-height: 32px; padding-top: 18px;
  }
</style>
</head>
<body>
<main class="poster">
  <div class="bokeh-backdrop" role="img" aria-label="Dark purple and magenta bokeh lights with gold glitter sparkle"></div>

  <p class="presenter">Prairie Hearts for Life presents<br>the Tenth Annual Fundraising Banquet</p>

  <h1 class="title"><span>The Winter</span><span class="second">Lantern</span></h1>

  <div class="subtitle-box">A PRO-LIFE CHRISTMAS GALA</div>

  <p class="date">Saturday, November 21st, 2020</p>
  <p class="doors">Doors open at 5:30PM</p>
  <p class="venue">Hollis Meadow Hall, Maple Grove, IA</p>
  <p class="pricing">$60 person • $500 table of ten</p>

  <p class="highlights">Cocktails • Dinner • Christmas Concert</p>

  <p class="speaker-label">Special Guest Speaker</p>
  <p class="speaker-name">Bishop Thomas Aldine</p>

  <p class="seating">SEATING LIMITED • RESERVATIONS NEEDED</p>

  <footer class="footer">
    <p>Order tickets online: www.PrairieHeartsForLife.org</p>
    <p>515-555-0148 • events@prairieheartsforlife.org</p>
  </footer>
</main>
</body>
</html>
```